Brookfarrow Osteopathy and dry needling business card

Business card for Brookfarrow Osteopathy and Dry Needling.

Industry/Entity Type

Health

Contact Information for Business Card

I do not have a phone number yet. I also do not have an email address yet. The physical address is: 48 Lower Crane Street Brookfarrow The website is: www.brookfarrowosteosteopathy.example My details are: Dr Martin Pellowe, Osteopath (B.Clin.Sci (Ost) M.Ost BSC ECON (Hons)

Colors
0094D4
00A9DD
6FCCEA
C7EBF8
E9F6FB

Requirements
Must have
• logo on the back
Nice to have
• Maybe a space for me to write an appointment time and date on the card.

```html
<!DOCTYPE html>
<html lang="en">
<head>
<meta charset="utf-8">
<title>Brookfarrow Osteopathy and Dry Needling – Business Card</title>
<link rel="stylesheet" href="https://fonts.googleapis.com/css2?family=Montserrat:wght@300;400;500;700&display=swap">
<style>
  :root {
    --brand-blue: #0094D4;
    --sky-blue: #00A9DD;
    --soft-blue: #6FCCEA;
    --pale-blue: #C7EBF8;
    --mist-blue: #E9F6FB;
    --accent-orange: #F7941D;
    --peach: #FDD3A8;
    --ink: #4a4a4a;
    --muted: #7a7a7a;
    --backdrop: #959595;
    --paper: #ffffff;
  }
  * { box-sizing: border-box; margin: 0; padding: 0; }
  html, body {
    width: 1200px; height: 1000px; overflow: hidden;
    background: var(--backdrop);
    font-family: "Montserrat", sans-serif;
  }
  .stage { position: relative; width: 1200px; height: 1000px; }

  .card {
    position: absolute; left: 315px; width: 569px; height: 328px;
    border-radius: 28px; overflow: hidden;
  }
  .card--front { top: 145px; background: var(--brand-blue); }
  .card--back { top: 527px; background: var(--paper); }

  /* Front */
  .brand-mark {
    position: absolute; left: 0; right: 0; top: 60px;
    display: flex; flex-direction: column; align-items: center; gap: 12px;
    color: var(--paper);
  }
  .brand-mark__circle {
    width: 70px; height: 70px; border-radius: 50%;
    border: 2px solid var(--paper);
  }
  .brand-mark__name {
    font-weight: 500; font-size: 15px; letter-spacing: 2px;
    text-transform: uppercase; text-align: center; line-height: 1.5;
    color: var(--paper);
  }
  .website {
    position: absolute; left: 0; right: 0; top: 274px;
    text-align: center; font-size: 19px; letter-spacing: -0.2px;
  }
  .website__domain { color: var(--accent-orange); font-weight: 700; }
  .website__tld { color: var(--paper); font-weight: 400; }

  /* Back */
  .back-art {
    position: absolute; right: 0; top: 0; width: 300px; height: 100%;
    background:
      linear-gradient(to right, var(--paper) 0%, rgba(255,255,255,0) 45%),
      linear-gradient(to bottom, var(--paper) 0%, var(--peach) 35%, var(--pale-blue) 62%, var(--soft-blue) 78%, var(--paper) 100%);
    opacity: 0.75;
  }
  .contact {
    position: absolute; left: 0; width: 290px; top: 94px;
    text-align: center;
  }
  .contact__name {
    font-weight: 700; font-size: 19.5px; color: var(--brand-blue);
  }
  .contact__credentials {
    margin-top: 4px; font-size: 11px; letter-spacing: 1px;
    color: var(--ink); line-height: 14px; text-transform: uppercase;
  }
  .contact__icons {
    margin-top: 13px; display: flex; justify-content: center; gap: 2px;
  }
  .icon-badge { width: 23px; height: 23px; }
  .contact__line {
    font-weight: 300; font-size: 19px; color: var(--muted); line-height: 24px;
  }
  .contact__line--phone { margin-top: 8px; }
  .contact__rule {
    width: 52px; height: 2px; background: var(--accent-orange);
    margin: 10px auto 0;
  }
  .contact__address {
    margin-top: 12px; font-size: 11.5px; color: var(--muted);
  }
</style>
</head>
<body>
<main class="stage">

  <section class="card card--front">
    <div class="brand-mark">
      <div class="brand-mark__circle"></div>
      <p class="brand-mark__name">Brookfarrow Osteopathy<br>&amp; Dry Needling</p>
    </div>
    <p class="website"><span class="website__domain">brookfarrowosteosteopathy</span><span class="website__tld">.example</span></p>
  </section>

  <section class="card card--back">
    <div class="back-art" role="img" aria-label="Faint brand decoration: rising sun rays over a spine and waves"></div>
    <div class="contact">
      <h1 class="contact__name">Dr. Martin Pellowe</h1>
      <p class="contact__credentials">Osteopath (B.Clin.Sci (Ost)<br>M.Ost BSc Econ (Hons)</p>
      <div class="contact__icons">
        <svg class="icon-badge" viewBox="0 0 24 24" aria-label="Phone">
          <circle cx="12" cy="12" r="12" fill="var(--accent-orange)"/>
          <path d="M8.2 6.5c.5-.4 1.2-.3 1.5.2l1 1.7c.3.5.2 1.1-.2 1.4l-.7.5c.5 1.4 1.5 2.6 2.8 3.4l.6-.6c.4-.4 1-.4 1.4-.1l1.6 1.1c.5.3.6 1 .2 1.5l-.8.9c-.6.6-1.5.8-2.3.4-2.9-1.4-5-3.8-6-6.8-.3-.8 0-1.7.6-2.2z" fill="#fff"/>
        </svg>
        <svg class="icon-badge" viewBox="0 0 24 24" aria-label="Email">
          <circle cx="12" cy="12" r="12" fill="var(--accent-orange)"/>
          <rect x="6.5" y="8" width="11" height="8" rx="1.2" fill="#fff"/>
          <path d="M7 8.8l5 3.8 5-3.8" fill="none" stroke="var(--accent-orange)" stroke-width="1.2"/>
        </svg>
      </div>
      <p class="contact__line contact__line--phone">123 45678</p>
      <p class="contact__line">email@website.com</p>
      <div class="contact__rule"></div>
      <p class="contact__address">48 Lower Crane Street Brookfarrow</p>
    </div>
  </section>

</main>
</body>
</html>
```